Leaflet and introduction email. designer required

To redesign our existing leaflet to more resemble our website style. The leaflet is to be a two fold A4 leaflet / menu for perspective customers who want physical further info on our company.
Also to redesign our attached PDF document into a better design. It will be emailed as a HTML email brochure introducing our company, with design style and link to our website. Food images available in addition to what is on our website
Target Market(s)
schools, nurseries, hospitals, and offices. Also local London boroughs.
Industry/Entity Type
Catering
Font styles to use
Other font styles liked:
- Heiti SC Light or similiar
Requirements
Must have
- modern quality feel. established company.
- follow company and Logo colours primarily.
Nice to have
- see website for style and fonts. www.brightplatter.catering
Should not have
- childish fonts and clip-art. design traits of attached documents, they should look more similiar to website.

```html
<!DOCTYPE html>
<html lang="en">
<head>
<meta charset="utf-8">
<title>Bright Platter Catering – Spring Menu Leaflet</title>
<link rel="stylesheet" href="https://fonts.googleapis.com/css2?family=Libre+Baskerville:wght@400;700&family=Open+Sans:wght@300;400&display=swap">
<style>
  :root {
    --backdrop: #b4b4b4;
    --backdrop-dark: #8d8d8d;
    --paper: #ffffff;
    --paper-fold: #ececec;
    --ink: #2b2b2b;
    --ink-soft: #4a4a4a;
    --rule: #6b6b6b;
    --brand-green: #5aa845;
    --brand-grey: #5e5e5e;
  }
  * { box-sizing: border-box; margin: 0; padding: 0; }
  html, body { width: 1200px; height: 781px; overflow: hidden; }
  body {
    background: radial-gradient(ellipse at center, var(--backdrop) 0%, var(--backdrop-dark) 100%);
    font-family: "Open Sans", sans-serif;
    color: var(--ink);
    position: relative;
  }
  .leaflet {
    position: absolute;
    left: 45px; top: 88px;
    width: 1110px; height: 605px;
    display: flex; flex-direction: column;
    background: var(--paper);
    box-shadow: 0 18px 40px rgba(0,0,0,.35);
  }
  .panels { display: flex; height: 430px; }
  .panel {
    flex: 1;
    padding: 34px 30px 20px;
    position: relative;
  }
  .panel + .panel { border-left: 1px solid var(--paper-fold); }
  .panel--left { background: linear-gradient(90deg, #fafafa, var(--paper)); }
  .panel--middle { background: linear-gradient(90deg, #f3f3f3, var(--paper) 20%, #f6f6f6); }
  .section-title {
    font-family: "Libre Baskerville", serif;
    font-weight: 700;
    font-size: 17px;
    margin-bottom: 8px;
  }
  .dish {
    font-weight: 400;
    font-size: 15px;
    line-height: 1.3;
    color: var(--ink);
    margin-bottom: 8px;
  }
  .dish-note {
    font-weight: 300;
    font-size: 10.5px;
    line-height: 1.35;
    color: var(--ink-soft);
    margin-bottom: 22px;
  }
  .menu-title {
    font-family: "Libre Baskerville", serif;
    font-size: 46px;
    text-align: center;
    margin-bottom: 12px;
  }
  .double-rule {
    border-top: 1px solid var(--rule);
    border-bottom: 1px solid var(--rule);
    height: 4px;
    margin: 0 -30px 22px;
  }
  .brand {
    display: flex; align-items: center; justify-content: flex-end;
    gap: 10px;
    height: 70px;
    margin-bottom: 10px;
  }
  .brand-name {
    font-family: "Open Sans", sans-serif;
    font-weight: 400;
    font-size: 24px;
    line-height: 1;
    color: var(--brand-green);
    text-transform: uppercase;
    letter-spacing: 1px;
  }
  .brand-mark {
    width: 16px; height: 16px;
    border-radius: 50%;
    background: var(--brand-green);
  }
  .brand-tagline {
    text-align: right;
    font-size: 8px;
    letter-spacing: 1px;
    color: var(--brand-grey);
    margin: -18px 0 18px;
    text-transform: uppercase;
  }
  .photo-strip { display: flex; height: 175px; }
  .photo { height: 100%; }
  .photo--fruit { width: 230px; background: linear-gradient(135deg, #d9c7a0, #f2c14e 45%, #c98a4b); }
  .photo--quiche { width: 225px; background: linear-gradient(135deg, #e7d6a8, #b88a4a 50%, #4f7a34); }
  .photo--curry { width: 215px; background: linear-gradient(135deg, #8a7a6a, #e3c22f 40%, #b5532a 75%, #7a6d62); }
  .photo--sandwich { width: 230px; background: linear-gradient(135deg, #8f7b66, #f1e0b8 40%, #e9783a 70%, #f4ecdf); }
  .photo--dessert { width: 210px; background: linear-gradient(135deg, #7c6a58, #f4f1ea 45%, #f2b01e 70%, #efefef); }
</style>
</head>
<body>
  <article class="leaflet">
    <div class="panels">
      <section class="panel panel--left">
        <h2 class="section-title">Nursery Spring menu (Kids)</h2>
        <p class="dish">Fruity Cous Cous Salad incorporated with raisins, sweet peppers, red onions and sweetcorn perfect for a child's cold tea dish.</p>
        <p class="dish-note">(Light &amp; fluffy cous cous inspired by traditional Moroccan spices &amp; flavours, from cumin, to ground coriander, to paprika and fennel seeds. All mix in together and cook with added vegetable in a veg stock &amp; a touch of sundried tomato puree).</p>
        <h2 class="section-title">Office Spring Menu (Adult)</h2>
        <p class="dish">Salmon &amp; broccoli fishcakes, With rosemary and paprika potato wedges. Served with a fresh homemade lime &amp; cucumber salsa</p>
        <p class="dish-note">(The wonderful combination of the salmon panned together with broccoli in golden breadcrumbs shallow fried on either side till lightly browned. Freshly cut Maris pipers potato in into wedges, cooked then lightly dusted in rosemary, paprika &amp; crackled black pepper served with a fresh red homemade salsa mixed in thinly sliced cucumber &amp; lime juice for dipping)</p>
      </section>

      <section class="panel panel--middle">
        <h1 class="menu-title">Menu</h1>
        <div class="double-rule"></div>
        <p class="dish">Succulent Roast chicken breast, with crushed potatoes served with seasonal spring veg and pouring onion gravy.</p>
        <p class="dish-note">(Traditional Sunday English family roast, using Halal chicken soft tender breast accompanied with the perfect crushed new potatoes and in seasonal hearty vegetables drizzle over with sweet caramelised onion gravy).</p>
        <div class="double-rule"></div>
        <p class="dish">Ultimate Homemade Banana Cake Loaf, Served with a dusting of icing sugar.</p>
        <p class="dish-note">(Cooked with fair-trade bananas, with a sweeter aromatic taste at they over ripen state, releasing the aromas and developed deep flavour).</p>
      </section>

      <section class="panel panel--right">
        <div class="brand">
          <span class="brand-name">Bright Platter Catering</span>
          <span class="brand-mark"></span>
        </div>
        <p class="brand-tagline">Fresh school &amp; office catering</p>
        <div class="double-rule"></div>
        <p class="dish">Mouth-watering seasonal plum &amp; rhubarb crumble, served with the option of warm vanilla custard for pouring.</p>
        <p class="dish-note">(Homemade from scratch juicy plums &amp; in season rhubarb for the perfect red combination crumble, rich with depth and flavour, always a kids favourite with every spoon full).</p>
        <div class="double-rule"></div>
        <p class="dish">Curried Parsnip &amp; Carrot Soup.</p>
        <p class="dish-note">Served with a fresh coriander crème fraiche garnish. Topped with cheesy croutons (Traditional root vegetable filling soup with a curried theme twist, accompanied with a hint of the Mediterranean aromatic coriander flavour, finished with crisp golden croutons which has been lightly sautéed in butter)</p>
      </section>
    </div>

    <div class="photo-strip">
      <div class="photo photo--fruit" role="img" aria-label="Photo of a glass bowl of fresh fruit salad"></div>
      <div class="photo photo--quiche" role="img" aria-label="Photo of a quiche slice with green salad leaves"></div>
      <div class="photo photo--curry" role="img" aria-label="Photo of yellow rice and a chickpea curry in metal dishes"></div>
      <div class="photo photo--sandwich" role="img" aria-label="Photo of sandwiches topped with grated carrot"></div>
      <div class="photo photo--dessert" role="img" aria-label="Photo of a mango dessert in a glass cup on a saucer"></div>
    </div>
  </article>
</body>
</html>
```